Brochure for community platform NGO needed

We are a non-profit working on building the first community platform for refugees, supporters and organisations all over Europe to facilitate inclusion on a community level.

We need a brochure with nice design to show to other organisations, donors, etc.

The design should show our emphasis on community, participation, humanity and empowerment. It should communicate trustworthiness, optimism and equality.

Target Market(s)

locals and organisations supporting refugees in europe

Industry/Entity Type

Non-Profit

Requirements
Must have
• our logo
Nice to have
• design representing the idea - something with bridges or puzzle pieces, something showing community, diversity, participation, etc.
Should not have
• stereotypical representations

```html
<!DOCTYPE html>
<html lang="en">
<head>
<meta charset="utf-8">
<title>PONTARA Brochure Spread</title>
<link href="https://fonts.googleapis.com/css2?family=Barlow+Semi+Condensed:wght@300;400;700&display=swap" rel="stylesheet">
<style>
  :root {
    --navy: #1e2f6e;
    --gold: #f2c230;
    --mustard: #dcae26;
    --ink: #2a3560;
    --white: #ffffff;
    --paper: #ffffff;
  }
  * { margin: 0; padding: 0; box-sizing: border-box; }
  html, body { width: 1200px; height: 854px; overflow: hidden; background: var(--paper); }
  body { font-family: "Barlow Semi Condensed", "Arial Narrow", sans-serif; font-weight: 300; }
  .spread { position: relative; width: 1200px; height: 854px; overflow: hidden; background: var(--paper); }

  .top-band { position: absolute; left: 0; top: 0; width: 1200px; height: 379px; background: var(--navy); }
  .gutter-shade {
    position: absolute; left: 600px; top: 379px; width: 70px; height: 475px;
    background: linear-gradient(to right, #d4d4d6 0%, #ececed 35%, rgba(255,255,255,0) 100%);
  }

  .col { position: absolute; font-size: 11.4px; line-height: 14.4px; letter-spacing: 0.25px; }
  .col p { text-align: justify; margin-bottom: 14.4px; }
  .col h2 { font-weight: 700; font-size: 17.4px; letter-spacing: 0.2px; margin-bottom: 21px; line-height: 20px; }
  .on-navy { color: var(--white); }
  .on-navy h2 { color: var(--gold); }
  .on-paper { color: var(--ink); }
  .on-paper h2 { color: var(--navy); margin-bottom: 24px; }

  .dots { list-style: none; margin-bottom: 14.4px; }
  .dots li { position: relative; padding-left: 10px; }
  .dots li::before {
    content: ""; position: absolute; left: 1px; top: 5px; width: 3px; height: 3px;
    border-radius: 50%; background: var(--gold);
  }
  .on-paper .dots li::before { background: var(--mustard); }
  .tight { letter-spacing: -0.15px; }

  .what { left: 48px; top: 34px; width: 240px; }
  .who { left: 332px; top: 34px; width: 234px; }
  .why { left: 638px; top: 34px; width: 522px; }
  .why .dots li { text-align: justify; }

  .look { left: 49px; top: 396px; width: 239px; }
  .look-cont { left: 332px; top: 438px; width: 234px; }
  .look-cont .dots li { text-align: justify; }
  .right-text { left: 659px; top: 438px; width: 490px; }

  .next-box {
    position: absolute; left: 649px; top: 547px; width: 505px; height: 99px;
    background: var(--mustard); color: var(--white);
    font-size: 11.4px; line-height: 14.4px; letter-spacing: 0.25px; padding: 5px 10px;
  }
  .next-box .dots li::before { background: var(--white); }

  .photo {
    position: absolute; left: 780px; top: 648px; width: 420px; height: 206px;
    background: radial-gradient(ellipse at 35% 40%, #e6e3df 0%, #e8b894 35%, #f3dcc8 60%, rgba(255,255,255,0) 80%);
  }
</style>
</head>
<body>
<div class="spread">
  <div class="top-band"></div>
  <div class="gutter-shade"></div>

  <section class="col on-navy what">
    <h2>WHAT IS PONTARA?</h2>
    <p>PONTARA is a European- wide platform that connects refugees, supporters and organisations to build a community and create huge impact, long- term, sustainable solutions together. It is an easy to use and highly cost- efficient tool to facilitate successful inclusion of refugees in Europe.</p>
    <p>The power of PONTARA lies in its strong ties with the community. Instead of professional “experts” creating top- down solutions for the target group, we are ourselves part of the target group, share their experience and maximize their participation.</p>
  </section>

  <section class="col on-navy who">
    <h2>WHO ARE WE?</h2>
    <p>PONTARA was created by Samir, a refugee from Syria, and Lena, a supporter from Vienna. We combined our experiences and perspectives to build a comprehensive solution for the many - faceted problems refugees and supporters encounter.</p>
    <p>The team of PONTARA covers many different backgrounds and experiences. All its members, no matter what their professional or personal background, share one thing: the belief that humanity enables us to overcome any obstacle.</p>
    <p>The many different fields of expertise of our team members are complemented by our friends and advisers from an even greater bandwidth of professional backgrounds, covering everything from web designers to high-ranking government officials.</p>
  </section>

  <section class="col on-navy why">
    <h2>WHY ARE WE BUILDING PONTARA?</h2>
    <p style="margin-bottom:0">With PONTARA, we are aiming at solving five key problems:</p>
    <ul class="dots">
      <li>Accessibility</li>
      <li>Participation</li>
      <li>Communication &amp; coordination</li>
      <li>Social life</li>
      <li>Scattered individual puzzle pieces without a big picture</li>
    </ul>
    <p style="margin-bottom:0">In our opinion, the solution lies in</p>
    <ul class="dots">
      <li>Building bridges between refugees and locals to create a social community online as well as offline</li>
      <li>Building bridges between initiatives and organisations to ease and facilitate coordination and cooperation between them</li>
      <li>Building bridges between the community and organisations to assure for accessibilty and participation and thus enable efficient use of resources and efforts</li>
    </ul>
    <p>This way, we will build a strong, empowered community of refugees and locals all over Europe and connect it with organisations while providing tools for all our platform members to solve the various problems they encounter. The main goal is to facilitate successful inclusion of refugees and immigrants into their new communities.</p>
  </section>

  <section class="col on-paper look">
    <h2>HOW WILL IT LOOK LIKE?</h2>
    <p>The platform will have two main sections, one for the community and one for organisations.</p>
    <p>PONTARA Community: Any individual can sign up to become a member of PONTARA community and use the Beta Version with the first basic features.</p>
    <p>Our technical team is right now working on developing the Beta Version and already preparing the development of the following features which will be available soon after the launch:</p>
    <ul class="dots">
      <li class="tight">Chose between arabic, english, farsi and german (with more languages to be added soon)</li>
      <li>Create a profile</li>
      <li>Connect with other individuals</li>
      <li class="tight">Use a geolocation map showing all organisations, services and points of interest for refugees and supporters</li>
      <li>Make additional entries in the map</li>
      <li>See organisational profiles</li>
      <li>Follow organisations to get updates</li>
      <li>See and attend volunteering requests and job postings from organisations</li>
      <li>Search for and attend events</li>
    </ul>
  </section>

  <section class="col on-paper look-cont">
    <ul class="dots">
      <li>Create events</li>
      <li>Join and create groups to exchange with other people with the same interests</li>
      <li class="tight">Find information on issues refugees are faced with</li>
      <li>Ask questions that are not answered yet and answer questions asked by others</li>
      <li class="tight">Apply to be part of the pontara team as translator</li>
      <li class="tight">Apply to be part of the pontara team and manage your local community as an ambassador</li>
    </ul>
    <p style="margin-bottom:0">PONTARA Circles: for any organisation, initiative, etc. to connect with other organisations and get in touch with the community</p>
    <ul class="dots">
      <li>Create a profile</li>
      <li>List your organisation in our geolocation feature</li>
      <li class="tight">Get an overview of the organisational landscape</li>
      <li class="tight">Connect with and message other organisations</li>
      <li>Post smart volunteering requests</li>
      <li class="tight">Access data from our surveys to better get to</li>
      <li class="tight">know the communities wishes, needs and ideas Create events</li>
      <li class="tight">Use your access to the community for fundraising</li>
    </ul>
    <p>PONTARA will thus serve as a starting point for refugees, locals and organisations all over Europe who want to find information of any</p>
  </section>

  <section class="col on-paper right-text">
    <p>kind in their language, participate in helping refugees, communicate and coordinate their work, get in touch with other people, get active by volunteering, finding volunteers to help with their workload, and so much more.</p>
    <p>The main goal is to create a big picture out of all the already existing individual puzzle pieces. We will make sure to continuously collect feedback, ideas and wishes from the community to constantly develop additional features according to the communities needs.</p>
  </section>

  <aside class="next-box">
    <p>Examples for what could be added next:</p>
    <ul class="dots">
      <li>Add additional languages</li>
      <li>Add businesses to the platform</li>
      <li>Circles: joint venture feature to help initiatives find partners to expand to new communities</li>
      <li>Circles: grants &amp; funds to connect organisations searching for funding with fund providers</li>
      <li>Circles &amp; Community: offer&amp;seek board</li>
    </ul>
  </aside>

  <div class="photo" role="img" aria-label="Photo of two hands holding a white puzzle-piece globe with one golden piece being placed"></div>
</div>
</body>
</html>
```